Duel Business card

Want an edgy business card that shows both of our companies on each side of the card, OR both together with a cool design.

*Must be edgy: We have attached our two business logos. We are a bail bond and immigration bond company.

Would like the address on one side only.
Need Phone, cell, website, address, and Name

Company Name 1: Cellgate Release Partners
www.cellgatereleasepartners.example

Company Name 2: Borderline Surety Associates
www.borderlinesuretyassociates.example

These cards will need to be easily changeable so I can modify new employees

Target Market(s)

people in jail, takign imigrants out of jail and from being taken back to there country

Industry/Entity Type

Business

Requirements
Must have
• Include both logos attached

```html
<!DOCTYPE html>
<html lang="en">
<head>
<meta charset="utf-8">
<title>Duel Business Cards</title>
<link rel="stylesheet" href="https://fonts.googleapis.com/css2?family=Marcellus+SC&display=swap">
<style>
  :root {
    --page-bg: #e9eaec;
    --red-light: #f0463c;
    --red-mid: #c8231e;
    --red-dark: #7e0f0c;
    --blue-deep: #1f3f8f;
    --blue-mid: #3a55a6;
    --gold: #f2c24e;
    --gold-soft: #e7b960;
    --navy-text: #14213f;
    --black: #0b0b0b;
    --white: #ffffff;
  }
  * { box-sizing: border-box; margin: 0; padding: 0; }
  html, body {
    width: 1068px; height: 1200px; overflow: hidden;
    background: var(--page-bg);
    font-family: "Marcellus SC", "Times New Roman", serif;
  }
  .card-pair {
    position: absolute; inset: 0;
    display: flex; justify-content: center; align-items: center; gap: 52px;
  }
  .card {
    position: relative; width: 460px; height: 805px; overflow: hidden;
    box-shadow: 0 10px 30px rgba(0,0,0,.25);
    text-align: center;
  }
  .card--immigration {
    background: linear-gradient(160deg, var(--red-dark) 0%, var(--red-mid) 30%, var(--red-light) 60%, var(--red-mid) 100%);
    color: var(--white);
  }
  .card--bail {
    background: linear-gradient(180deg, var(--blue-deep) 0%, var(--blue-mid) 22%, var(--gold) 50%, var(--gold-soft) 62%, var(--blue-mid) 85%, var(--blue-deep) 100%);
    color: var(--navy-text);
  }
  .card__sides { position: absolute; inset: 0; }
  .card__content { position: relative; z-index: 1; height: 100%; }
  .logo-mark {
    display: block; width: 104px; height: 104px; border-radius: 50%;
    margin: 40px auto 0;
  }
  .card--immigration .logo-mark { background: var(--white); border: 6px solid var(--red-dark); }
  .card--bail .logo-mark { background: var(--white); border: 6px solid var(--gold); }
  .company-name {
    margin-top: 26px; font-size: 28px; font-weight: 400; letter-spacing: .5px;
  }
  .card--immigration .company-name { color: var(--white); }
  .card--bail .company-name { color: var(--navy-text); }
  .person { margin-top: 76px; }
  .person__name { font-size: 46px; font-weight: 400; line-height: 1; color: var(--black); }
  .person__position { font-size: 13px; margin-top: 6px; color: var(--black); }
  .contact {
    position: absolute; left: 0; right: 0; bottom: 70px;
    font-size: 17px; line-height: 1.6;
  }
  .card--immigration .contact { color: var(--white); bottom: 90px; }
  .card--bail .contact { color: var(--gold); }
  .contact p { white-space: nowrap; }
</style>
</head>
<body>
<main class="card-pair">

  <article class="card card--immigration">
    <svg class="card__sides" viewBox="0 0 460 805" preserveAspectRatio="none" aria-hidden="true">
      <path fill="#0b0b0b" d="M0 300 C150 340 195 520 172 640 C158 720 110 780 70 805 L0 805 Z"/>
      <path fill="#0b0b0b" d="M460 300 C310 340 265 520 288 640 C302 720 350 780 390 805 L460 805 Z"/>
    </svg>
    <div class="card__content">
      <span class="logo-mark" aria-hidden="true"></span>
      <h2 class="company-name">BORDERLINE SURETY ASSOCIATES</h2>
      <div class="person">
        <h1 class="person__name">FIRSTNAME SURNAME</h1>
        <p class="person__position">POSITION</p>
      </div>
      <div class="contact">
        <p>1234 ADRESS LANE ADRESS CITY, EX 12345</p>
        <p>PHONE: 877-555-0142 &nbsp;CELL PHONE: 555-010-789</p>
        <p>INFO@BORDERLINESURETYASSOCIATES.EXAMPLE</p>
        <p>WWW.BORDERLINESURETYASSOCIATES.EXAMPLE</p>
      </div>
    </div>
  </article>

  <article class="card card--bail">
    <svg class="card__sides" viewBox="0 0 460 805" preserveAspectRatio="none" aria-hidden="true">
      <path fill="#0b0b0b" d="M0 370 C130 400 165 560 150 660 C140 730 100 780 70 805 L0 805 Z"/>
      <path fill="#0b0b0b" d="M460 370 C330 400 295 560 310 660 C320 730 360 780 390 805 L460 805 Z"/>
    </svg>
    <div class="card__content">
      <span class="logo-mark" aria-hidden="true"></span>
      <h2 class="company-name">CELLGATE RELEASE PARTNERS</h2>
      <div class="person">
        <h1 class="person__name">FIRSTNAME SURNAME</h1>
        <p class="person__position">POSITION</p>
      </div>
      <div class="contact">
        <p>PHONE: 1-888-555-0187 &nbsp;CELL PHONE: 555-010-789</p>
        <p>INFO@CELLGATERELEASEPARTNERS.EXAMPLE</p>
        <p>WWW.CELLGATERELEASEPARTNERS.EXAMPLE</p>
      </div>
    </div>
  </article>

</main>
</body>
</html>
```